Fenwick Creek Rodeo Sponsor Brochure/letter

We are wanting a professional looking brochure/letter that can be given to potential sponsors. This can be multiple pages the last page needs to be the Invoice (attached example) the prices on the example can be used.. this is a first nation rodeo and we are looking for sponsorship I can provide more photos if needed

Target Market(s)

This will be local corporate business's so this needs to be very professional looking

Industry/Entity Type

This is an event but we are looking for cooperate sponsorship

Font styles to use
Serif

Colors
0054AA
0677BA
7BADD7
CADEEF
E8F1F8
FFC000
F8CF3A
FAE287
FDF2CF
FEFAEE
F0912C
F2A743
F7CA91
FBE8D2
FDF5EE
EB3D1F
EC4F4E
F09395
F8D3D4
FCEDEE

Requirements
Must have
• The basic information, must have some quotes and photos can be multiple pages
Nice to have
• I would like to see that it is interactive, but gets to the point
Should not have
• no cartoon or must not look cheap

```html
<!DOCTYPE html>
<html lang="en">
<head>
<meta charset="utf-8">
<title>Fenwick Creek Rodeo – Sponsorship Letter</title>
<link rel="stylesheet" href="https://fonts.googleapis.com/css2?family=Source+Serif+4:wght@400;700&display=swap">
<style>
  :root {
    --brand-blue: #0054AA;
    --brand-orange: #F0912C;
    --ink-light: #FFFFFF;
    --photo-dust: #8a6a4e;
    --photo-sky: #b9b2a6;
    --photo-grass: #7d7a4c;
  }
  * { margin: 0; padding: 0; box-sizing: border-box; }
  html, body { width: 1020px; height: 1200px; overflow: hidden; }
  body {
    background: var(--brand-blue);
    font-family: "Source Serif 4", Georgia, serif;
    color: var(--ink-light);
  }
  .brochure { position: relative; width: 1020px; height: 1200px; overflow: hidden; }
  .backdrop { position: absolute; inset: 0; width: 1020px; height: 1200px; }

  .events-title {
    position: absolute; left: 700px; top: 26px; width: 150px;
    text-align: center; font-weight: 700; font-size: 23px; letter-spacing: 0.5px;
  }
  .event-row { position: absolute; left: 569px; display: flex; font-weight: 700; font-size: 19.5px; line-height: 24px; }
  .event-date { width: 96px; flex: none; }
  .event-detail { width: 340px; }
  .row-28 { top: 76px; }
  .row-29 { top: 120px; }
  .row-30 { top: 236px; }

  .extras {
    position: absolute; left: 676px; top: 318px; width: 340px;
    font-weight: 700; font-size: 15.5px; line-height: 20px;
  }
  .extras p + p { margin-top: 5px; }

  .letter {
    position: absolute; left: 46px; top: 580px; width: 603px;
    font-size: 15.6px; line-height: 20px; text-align: justify;
  }
  .letter p + p { margin-top: 10px; }

  .welcome {
    position: absolute; left: 716px; top: 572px; width: 290px;
    font-weight: 700; font-size: 19.6px; line-height: 24px;
  }

  .contact {
    position: absolute; left: 300px; top: 1088px; width: 349px;
    text-align: right; font-size: 15.6px; line-height: 20px;
  }
  .contact-heading { font-weight: 700; margin-bottom: 10px; }

  .nation-name {
    position: absolute; left: 760px; top: 1080px; display: flex; align-items: center; gap: 12px;
    font-weight: 700; font-size: 22px; line-height: 26px; color: var(--ink-light);
  }
  .nation-mark { width: 34px; height: 34px; border-radius: 50%; background: var(--ink-light); flex: none; }
</style>
</head>
<body>
<main class="brochure">
  <svg class="backdrop" viewBox="0 0 1764 2075" aria-hidden="false">
    <defs>
      <linearGradient id="rodeo-photo-tone" x1="0" y1="0" x2="0" y2="1">
        <stop offset="0" stop-color="#b9b2a6"/>
        <stop offset="0.4" stop-color="#7d7a4c"/>
        <stop offset="0.6" stop-color="#8a6a4e"/>
        <stop offset="1" stop-color="#6e5340"/>
      </linearGradient>
    </defs>
    <polygon class="photo-area" role="img" aria-label="Photo of a bronc rider on a bucking paint horse in the rodeo arena"
      points="0,0 615,0 1205,915 1150,970 0,970" fill="url(#rodeo-photo-tone)"/>
    <polygon class="events-panel" points="615,0 1764,0 1764,325 1560,537 1148,537 1148,713 1393,713 1205,915" fill="#F0912C"/>
  </svg>

  <h2 class="events-title">-&nbsp;&nbsp;EVENTS&nbsp;&nbsp;-</h2>
  <div class="event-row row-28"><span class="event-date">July 28</span><span class="event-detail">Gymkhana and family Dance</span></div>
  <div class="event-row row-29"><span class="event-date">July 29</span><span class="event-detail">Junior Rodeo at 11 am, Main Rodeo starts at 2 pm with Steak Dinner and Rodeo dance to follow Band is The Timber Lines</span></div>
  <div class="event-row row-30"><span class="event-date">July 30</span><span class="event-detail">Junior Rodeo at 11 am, Main Rodeo starts at 2 pm</span></div>

  <div class="extras">
    <p>Free Pancake Breakfast both Saturday and Sunday Morning.</p>
    <p>Cultural Events happening throughout the day.</p>
  </div>

  <section class="letter">
    <p>2 One day Rodeos with amazing prizes and buckles each day with the average winning a FCFN Drum! The Fenwick Creek Rodeo is an attraction to many local cowboys and cowgirls from local communities, Fort St. John and across BC, AB and surrounding areas. We offer youth to adult events that are all crowd pleasers.</p>
    <p>Since the beginning this has been an annual event up until Covid-19 when we have had to take a break but we are so excited to build it bigger and better then before!</p>
    <p>We have some big plans for the future of the Fenwick Creek Rodeo including an expansion of the Rodeo grounds, new event buildings, new office/announcer booths as well as the purchase of new grandstands. This will be a big endeavor that we think will benefit both our community as well as the local community.</p>
    <p>Our rodeo would not have flourished without the support and generosity we have received from your sponsorship over the years. Once again, we are hoping your company will give generously to our yearly event and help continue to make our rodeo a success. All support goes towards any supplies not covered by donation, the purchase of materials to upgrade the rodeo grounds, rodeo stock and event payout. We hope to attract even more rodeo events, larger entertainers, and more fans through the gates. Your sponsorship will be highly regarded for what we hope will be generations to come.</p>
    <p>Please see the level of sponsorship attached, fill and return to the Fenwick Creek Rodeo!</p>
    <p>Your sponsorship is greatly appreciated.</p>
  </section>

  <p class="welcome">Saddle up for the Fenwick Creek Rodeo held at the Fenwick Creek First Nation Rodeo grounds! This is now a 3 day family fun event with the addition of a Friday afternoon Gymkhana! Fenwick Creek Rodeo has been running for over 30 years and we are exciting to bring the excitement back.</p>

  <div class="contact">
    <p class="contact-heading">For further information please call or email</p>
    <p>Marla Tennant&nbsp;&nbsp;|&nbsp;&nbsp;250.555.0147</p>
    <p>mtennant@fenwickcreekfn.com</p>
  </div>

  <div class="nation-name"><span class="nation-mark"></span><span>FENWICK CREEK<br>FIRST NATION</span></div>
</main>
</body>
</html>
```